Learning Uplift Collective Website

Background

Learning Uplift Collective (LUC) is a newly established consultancy that focuses on education, primarily improving schools and universities. The company is registered in Dubai.

Domain name is learnuplift.com, the logo for LUC is attached as is the registered business address

Scope

LUC requests designers to design and build a website that initially includes the following key pages/sections.

• About us/our story
• Our people
• Our services
• Our work
• Contact us/social media

Some examples of websites that are similar to the look and feel of a new contemporary startup like LUC include the following:
http://www.tarvel.co/journal/
https://www.mizrenadvisory.com/

Content to be provided by LUC. In addition, LUC wishes the successful designer to set up all email and social media accounts required.

Target Market(s)

Government Education departments, donors, Private school chains, school owners, NGOs, investors

Industry/Entity Type

Education

Number of Pages Required

3 page

Font styles to use
Sans Serif

Colors

Designer to choose colors to be used in the design.

Requirements
Must have
• • About us/our story
• • Our people
• • Our services
• • Our work
• • Contact us/social media
• (Maximum 3 pages)
• domain name, address, our services etc
• Blend colours with logo design colours
Nice to have
• Given the migration to mobile devices, we think that having a site which can be scrolled from top to bottom would be preferable
• Possibly a lite version in areas where bandwidth is poor?
Should not have
• Anything that takes a long time to download

```html
<!DOCTYPE html>
<html lang="en">
<head>
<meta charset="utf-8">
<title>Learning Uplift Collective</title>
<link href="https://fonts.googleapis.com/css2?family=Nunito+Sans:wght@300;400;600;700&family=Open+Sans:wght@400;700&display=swap" rel="stylesheet">
<style>
:root{
  --brand:#2f3f8f;
  --brand-deep:#1f2a66;
  --ink:#333a44;
  --muted:#6b717a;
  --soft:#f5f5f6;
  --footer:#f1f1f2;
  --line:#d9dadd;
  --white:#ffffff;
}
*{box-sizing:border-box;margin:0;padding:0}
html,body{width:1200px;height:3327px;overflow:hidden}
body{font-family:"Nunito Sans",Arial,sans-serif;color:var(--ink);background:var(--white);position:relative}
.section{position:absolute;left:0;width:1200px}
.section-title{font-weight:300;font-size:36px;letter-spacing:1px;text-align:center;color:#2a2e35;text-transform:uppercase}

/* header */
.site-header{top:0;height:102px;background:var(--white);box-shadow:0 2px 6px rgba(0,0,0,.12);z-index:3}
.brand{position:absolute;left:100px;top:36px;height:30px;display:flex;align-items:center;gap:10px;color:var(--brand);font-weight:700;font-size:22px;white-space:nowrap}
.brand-square{width:20px;height:20px;background:var(--brand);flex:none}
.main-nav{position:absolute;right:96px;top:32px;height:38px;display:flex;align-items:center;gap:34px}
.main-nav a{position:relative;font-size:13px;line-height:20px;color:#333;text-decoration:none;letter-spacing:.3px;white-space:nowrap}
.main-nav a.active{color:var(--brand)}
.main-nav a.active::after{content:"";position:absolute;left:0;right:0;bottom:-16px;height:2px;background:var(--brand)}
.main-nav a.cta{border:1px solid #bbb;border-radius:3px;padding:8px 12px}

/* hero */
.hero{top:102px;height:598px;overflow:hidden}
.hero-photo{position:absolute;inset:0;background:linear-gradient(180deg,#3a3d4a 0%,#6d6a73 38%,#8a7f86 55%,#2c2c3a 100%)}
.hero-title{position:absolute;top:192px;width:100%;text-align:center;font-family:"Open Sans",Arial,sans-serif;font-weight:700;font-size:40px;color:var(--white);letter-spacing:.5px}
.hero-text{position:absolute;top:250px;left:250px;width:700px;text-align:center;font-family:"Open Sans",Arial,sans-serif;font-size:17px;line-height:28px;color:var(--white)}
.hero-arrow{position:absolute;top:225px;width:36px;height:36px}
.hero-curve{position:absolute;left:0;bottom:0;width:1200px;height:70px}

/* about */
.about{top:700px;height:270px;text-align:center}
.about .section-title{margin-top:34px}
.about p{font-size:13px;color:var(--muted);line-height:24px;width:900px;margin:22px auto 0}
.about p.countries{margin-top:30px}

/* services */
.services{top:970px;height:401px;background:var(--soft)}
.services .section-title{margin-top:52px}
.service-list{position:absolute;top:155px;left:0;width:1200px}
.service{position:absolute;width:200px;text-align:center;transform:translateX(-100px)}
.service-icon{width:94px;height:94px;border-radius:50%;background:var(--brand);margin:0 auto;border:3px solid var(--white);box-shadow:0 0 0 2px var(--brand);display:flex;align-items:center;justify-content:center}
.service-name{font-size:14px;line-height:22px;margin-top:14px;color:#3a3f47}

/* provide */
.provide{top:1371px;height:505px;overflow:hidden}
.provide-photo{position:absolute;inset:0;background:linear-gradient(160deg,#4658a8 0%,#3a4b99 45%,#2e3d86 100%)}
.provide .section-title{position:absolute;top:58px;width:100%;color:var(--white)}
.provide-sub{position:absolute;top:110px;width:100%;text-align:center;font-size:12px;color:#e6e9f5}
.provide-list{position:absolute;top:166px;list-style:none}
.provide-list li{height:31px;font-size:13px;color:var(--white);display:flex;align-items:center;gap:8px}
.provide-list svg{flex:none}

/* people */
.people{top:1876px;height:692px;background:#f8f8f8}
.people .section-title{margin-top:66px}
.person{position:absolute;top:160px;width:450px;text-align:center}
.person-photo{width:333px;height:257px;margin:0 auto;background:linear-gradient(180deg,#cfcfcf,#9d9d9d)}
.person-name{font-size:23px;color:var(--brand-deep);margin-top:34px}
.person-role{font-size:13px;color:var(--muted);margin-top:2px}
.person-bio{font-size:12px;font-style:italic;color:#444;line-height:22px;margin:14px auto 0;width:440px}

/* work */
.work{top:2568px;height:366px;text-align:center}
.work .section-title{margin-top:66px}
.work p{font-size:13px;color:var(--muted);line-height:22px;width:960px;margin:24px auto 0}
.work p + p{margin-top:24px}

/* footer */
.site-footer{top:2934px;height:393px;background:var(--footer)}
.footer-col{position:absolute;top:44px}
.footer-col h4{font-weight:400;font-size:17px;color:#2a2e35;margin-bottom:18px}
.footer-col p,.footer-col a{display:block;font-size:13px;color:#555;line-height:30px;text-decoration:none}
.footer-divider{position:absolute;top:44px;width:1px;height:270px;background:var(--line)}
.map-box{width:200px;height:87px;border:2px solid var(--white);background:linear-gradient(135deg,#e4e4e2,#cfd3d6)}
.social{display:flex;gap:8px;margin-top:12px}
.social span{width:34px;height:34px;border-radius:50%}
.footer-bottom{position:absolute;left:100px;top:309px;width:1000px;border-top:1px solid var(--line);padding-top:30px;font-size:12px;color:#555}
</style>
</head>
<body>

<header class="section site-header">
  <div class="brand"><span class="brand-square"></span>Learning Uplift Collective</div>
  <nav class="main-nav">
    <a class="active" href="#">HOME</a>
    <a href="#">ABOUT US</a>
    <a href="#">OUR PEOPLE</a>
    <a href="#">OUR SERVICES</a>
    <a href="#">OUR WORK</a>
    <a class="cta" href="#">CONTACT US</a>
  </nav>
</header>

<section class="section hero">
  <div class="hero-photo" role="img" aria-label="Business team silhouetted against tall office windows"></div>
  <svg class="hero-arrow" style="left:18px" viewBox="0 0 36 36"><circle cx="18" cy="18" r="18" fill="rgba(255,255,255,.25)"/><path d="M21 10l-8 8 8 8" stroke="#fff" stroke-width="2" fill="none"/></svg>
  <svg class="hero-arrow" style="right:18px" viewBox="0 0 36 36"><path d="M15 10l8 8-8 8" stroke="#fff" stroke-width="2" fill="none"/></svg>
  <h1 class="hero-title">LEARNING UPLIFT COLLECTIVE (LUC)</h1>
  <p class="hero-text">Learning Uplift Collective (LUC) is a newly established consultancy in Dubai, UAE that focuses on education, primarily improving schools and universities</p>
  <svg class="hero-curve" viewBox="0 0 1200 70" preserveAspectRatio="none"><path d="M0 70 L0 20 Q600 -20 1200 20 L1200 70 Z" fill="#fff"/></svg>
</section>

<section class="section about">
  <h2 class="section-title">About Us/Our Story</h2>
  <p>The Partners have extensive international educational consultancy experience and have worked extensively improving schools, universities, education systems with delivery in the following countries</p>
  <p class="countries">United Kingdom, Australia, Germany, United States, Bahrain, U.A.E, Pakistan, India, South Africa, Saudi Arabia, Jordan.</p>
</section>

<section class="section services">
  <h2 class="section-title">Our Services</h2>
  <div class="service-list">
    <div class="service" style="left:195px">
      <div class="service-icon"><svg width="40" height="40" viewBox="0 0 40 40" fill="#fff"><circle cx="20" cy="12" r="7"/><rect x="8" y="22" width="24" height="14" rx="4"/></svg></div>
      <div class="service-name">Learning Uplift Collective Design</div>
    </div>
    <div class="service" style="left:395px">
      <div class="service-icon"><svg width="40" height="40" viewBox="0 0 40 40" fill="#fff"><path d="M4 14L20 5l16 9z"/><rect x="8" y="16" width="4" height="14"/><rect x="15" y="16" width="4" height="14"/><rect x="22" y="16" width="4" height="14"/><rect x="29" y="16" width="4" height="14"/><rect x="4" y="31" width="32" height="4"/></svg></div>
      <div class="service-name">Deliver and Support Government Education Systems</div>
    </div>
    <div class="service" style="left:610px">
      <div class="service-icon"><svg width="42" height="40" viewBox="0 0 42 40" fill="#fff"><path d="M2 15L21 7l19 8-19 8z"/><path d="M10 20v8c0 3 5 5 11 5s11-2 11-5v-8l-11 5z"/></svg></div>
      <div class="service-name">Public and Private Universities</div>
    </div>
    <div class="service" style="left:823px">
      <div class="service-icon"><svg width="42" height="40" viewBox="0 0 42 40" fill="#fff"><path d="M14 14l7-7 7 7v20H14z"/><rect x="4" y="20" width="9" height="14"/><rect x="29" y="20" width="9" height="14"/></svg></div>
      <div class="service-name">Groups of Private Schools</div>
    </div>
    <div class="service" style="left:1040px">
      <div class="service-icon"><svg width="40" height="40" viewBox="0 0 40 40" fill="#fff"><circle cx="12" cy="12" r="5"/><rect x="5" y="19" width="14" height="14" rx="3"/><rect x="22" y="8" width="14" height="11"/><rect x="24" y="22" width="10" height="11"/></svg></div>
      <div class="service-name">Individual Schools</div>
    </div>
  </div>
</section>

<section class="section provide">
  <div class="provide-photo" role="img" aria-label="Meeting room with people at a table under a blue tint"></div>
  <h2 class="section-title">What We Provide</h2>
  <p class="provide-sub">All support is contextualised and delivered with the client and at the highest standards possible</p>
  <ul class="provide-list" style="left:137px">
    <li><svg width="13" height="13" viewBox="0 0 13 13"><circle cx="6.5" cy="6.5" r="6.5" fill="#fff"/><path d="M3.5 6.7l2 2 4-4" stroke="#3a4b99" stroke-width="1.6" fill="none"/></svg>Support in developing strategy across a range of functional areas</li>
    <li><svg width="13" height="13" viewBox="0 0 13 13"><circle cx="6.5" cy="6.5" r="6.5" fill="#fff"/><path d="M3.5 6.7l2 2 4-4" stroke="#3a4b99" stroke-width="1.6" fill="none"/></svg>School improvement planning</li>
    <li><svg width="13" height="13" viewBox="0 0 13 13"><circle cx="6.5" cy="6.5" r="6.5" fill="#fff"/><path d="M3.5 6.7l2 2 4-4" stroke="#3a4b99" stroke-width="1.6" fill="none"/></svg>Education reform</li>
    <li><svg width="13" height="13" viewBox="0 0 13 13"><circle cx="6.5" cy="6.5" r="6.5" fill="#fff"/><path d="M3.5 6.7l2 2 4-4" stroke="#3a4b99" stroke-width="1.6" fill="none"/></svg>Teacher training design and delivery</li>
    <li><svg width="13" height="13" viewBox="0 0 13 13"><circle cx="6.5" cy="6.5" r="6.5" fill="#fff"/><path d="M3.5 6.7l2 2 4-4" stroke="#3a4b99" stroke-width="1.6" fill="none"/></svg>Curriculum</li>
    <li><svg width="13" height="13" viewBox="0 0 13 13"><circle cx="6.5" cy="6.5" r="6.5" fill="#fff"/><path d="M3.5 6.7l2 2 4-4" stroke="#3a4b99" stroke-width="1.6" fill="none"/></svg>Assessment</li>
    <li><svg width="13" height="13" viewBox="0 0 13 13"><circle cx="6.5" cy="6.5" r="6.5" fill="#fff"/><path d="M3.5 6.7l2 2 4-4" stroke="#3a4b99" stroke-width="1.6" fill="none"/></svg>School leadership training</li>
    <li><svg width="13" height="13" viewBox="0 0 13 13"><circle cx="6.5" cy="6.5" r="6.5" fill="#fff"/><path d="M3.5 6.7l2 2 4-4" stroke="#3a4b99" stroke-width="1.6" fill="none"/></svg>Supporting public-private partnerships in education</li>
  </ul>
  <ul class="provide-list" style="left:592px">
    <li><svg width="13" height="13" viewBox="0 0 13 13"><circle cx="6.5" cy="6.5" r="6.5" fill="#fff"/><path d="M3.5 6.7l2 2 4-4" stroke="#3a4b99" stroke-width="1.6" fill="none"/></svg>School inspection</li>
    <li><svg width="13" height="13" viewBox="0 0 13 13"><circle cx="6.5" cy="6.5" r="6.5" fill="#fff"/><path d="M3.5 6.7l2 2 4-4" stroke="#3a4b99" stroke-width="1.6" fill="none"/></svg>Instructional supervision</li>
    <li><svg width="13" height="13" viewBox="0 0 13 13"><circle cx="6.5" cy="6.5" r="6.5" fill="#fff"/><path d="M3.5 6.7l2 2 4-4" stroke="#3a4b99" stroke-width="1.6" fill="none"/></svg>Coaching and feedback to elevate individual and team performance</li>
    <li><svg width="13" height="13" viewBox="0 0 13 13"><circle cx="6.5" cy="6.5" r="6.5" fill="#fff"/><path d="M3.5 6.7l2 2 4-4" stroke="#3a4b99" stroke-width="1.6" fill="none"/></svg>Strategy to improve university rankings</li>
    <li><svg width="13" height="13" viewBox="0 0 13 13"><circle cx="6.5" cy="6.5" r="6.5" fill="#fff"/><path d="M3.5 6.7l2 2 4-4" stroke="#3a4b99" stroke-width="1.6" fill="none"/></svg>Organisational transformation</li>
    <li><svg width="13" height="13" viewBox="0 0 13 13"><circle cx="6.5" cy="6.5" r="6.5" fill="#fff"/><path d="M3.5 6.7l2 2 4-4" stroke="#3a4b99" stroke-width="1.6" fill="none"/></svg>Designing Performance Appraisal Systems</li>
    <li><svg width="13" height="13" viewBox="0 0 13 13"><circle cx="6.5" cy="6.5" r="6.5" fill="#fff"/><path d="M3.5 6.7l2 2 4-4" stroke="#3a4b99" stroke-width="1.6" fill="none"/></svg>Assessment of institutions and development of Institutional Strengthening Plans</li>
    <li><svg width="13" height="13" viewBox="0 0 13 13"><circle cx="6.5" cy="6.5" r="6.5" fill="#fff"/><path d="M3.5 6.7l2 2 4-4" stroke="#3a4b99" stroke-width="1.6" fill="none"/></svg>Targeted support (such as interviewing for key leadership positions)</li>
  </ul>
</section>

<section class="section people">
  <h2 class="section-title">Our People</h2>
  <div class="person" style="left:101px">
    <div class="person-photo" role="img" aria-label="Black and white portrait of the CEO"></div>
    <h3 class="person-name">Numquam Eius Modi</h3>
    <p class="person-role">(CEO)</p>
    <p class="person-bio">But I must explain to you how all this mistaken idea of denouncing pleasure and praising pain was born and I will give you a complete account of the system, and expound the actual teachings of the great explorer of the truth, the master-builder of human happiness.</p>
  </div>
  <div class="person" style="left:649px">
    <div class="person-photo" role="img" aria-label="Black and white portrait of the Executive Director"></div>
    <h3 class="person-name">Nihil Molestiae Consequatur</h3>
    <p class="person-role">(Executive Director)</p>
    <p class="person-bio">But I must explain to you how all this mistaken idea of denouncing pleasure and praising pain was born and I will give you a complete account of the system, and expound the actual teachings of the great explorer of the truth, the master-builder of human happiness.</p>
  </div>
</section>

<section class="section work">
  <h2 class="section-title">Our Work</h2>
  <p>The Partners have extensive experience in large-scale education reform across the K-12 and higher education sectors. These experiences have included work within advanced and emerging economy countries, as well systems with more than 50,000 schools.</p>
  <p>Impact is a core pillar of the education reform contributions from both partners, from improving student, teacher and school performance, through to improving university reform in short periods of time. LUC have access to a range of high caliber and skilled consultants who are matched with the needs of the engagement and required scope of work.</p>
</section>

<footer class="section site-footer">
  <div class="footer-col" style="left:100px">
    <h4>Our Map</h4>
    <div class="map-box" role="img" aria-label="Street map showing the office location"></div>
  </div>
  <div class="footer-divider" style="left:362px"></div>
  <div class="footer-col" style="left:404px">
    <h4>Contact Address</h4>
    <p>Business Center,</p>
    <p>Al Rimal Building,</p>
    <p>Coastal Free Trade Zone,</p>
    <p>Al Sahil, U.A.E.</p>
    <h4 style="margin-top:10px;margin-bottom:10px">Operating Name</h4>
    <p>Learning Uplift Collective FZC</p>
  </div>
  <div class="footer-divider" style="left:714px"></div>
  <div class="footer-col" style="left:752px">
    <h4>Quick Links</h4>
    <a href="#">About Us</a>
    <a href="#">Our People</a>
    <a href="#">Our Services</a>
    <a href="#">Our Work</a>
    <a href="#">Contact Us</a>
  </div>
  <div class="footer-divider" style="left:903px"></div>
  <div class="footer-col" style="left:943px">
    <h4>Follow Us</h4>
    <p>Please connect with us on</p>
    <div class="social">
      <span style="background:#3fa9e0"></span>
      <span style="background:#3b5a9a"></span>
      <span style="background:#1c7bb4"></span>
      <span style="background:#d9473a"></span>
    </div>
  </div>
  <div class="footer-bottom">© 2017 Learning Uplift Collective (LUC). All right reserved. Term of Use</div>
</footer>

</body>
</html>
```